Relaunch of company website (Technical company)

Hi all,

we need a website based on Wordpress who makes the customer curious and excited of all the possibilities we can offer.
Customers are B2B. The layout should be based on the screenshots I added, but refreshed and modernized with some nice gadgets.
All needs to be responsive for the different devices.
We are a technical company. We provide a full range of service from 3D scan, Manufacturing, Prototyping, Bulk production and CAD service.

Later the website needs to have a multi language option.

Home:

1. Logo top left (attached)
2. Menu bar top right
3. Header picture like in the screenshot
4. Than the three small blue pics (CAD - Fertigung - Manufaktur) we want a
hoover-small zoom effect as soon as the mouse hits them.
5. Introduction text of our company
6. Contact Information (Design sample see attachment)
7. At the end "Impressum - Datenschutzerklärung - Haftungsausschluss. Those need to be linked to extra pages where we can add mandatory text (Legal notice, Privacy, Disclaimer)

Leistungen - Our service:

1. See the attachment named our service.
2. First on page a gallery where we can add pictures. If moving the mouse over the picture we want a one line explanation e.g. 3D Scan, Production, Die cast...
no click option at the pictures, just to see.
3. Below that, a side menu (we need to add or remove items by our self if necessary) on the left where we can add our service.
4. If the customer is clicking a service, it needs to be highlighted
5. After clicking a service we want our text to that service appear right of the menu (see attachment sample) and 2 big pictures on top of the menu and text field.

Gallery:

1. Headline pictures for each gallery Category (6-8 at the moment)
2. Mouse over the picture zooms it a little in and adds a text what category it is
e.g. Reverse engineering, Prototyping, Laserscan
3. Clicking on the picture opens the detail gallery to that category. There we need
to add pictures specific to that service.
4. If the customer is clicking on a picture from there, all pictures from that
Category will open in a full screen view mode

Blog:

1. A blog to add news (picture and text). Right now we don´t have the time to feed
it, so we want to deactivate it as long as we cant keep it up to date. Later it
should be part of the website.

Unternehmen:

1. Drop down menu: Our Team - History - Unsere Partner - AGB - Impressum

Our Team:
1. Short description of our employees including picture (see attachment)
2. Contact Information (Design sample see attachment)
3. At the end "Impressum - Datenschutzerklärung - Haftungsausschluss. Those need to be linked to extra pages where we can add mandatory text (Legal notice, Privacy, Disclaimer)

History:
1. Timeline where we can add milestones including date, and pictures of the company (see screenshot)

Unsere Partner:
1. Text field where we can introduce our partners including pictures if necessary.

A blog would be a nice option, social media shortcuts to Instagram-FB but no preview of FB Timeline within the website.

We do have professional text already, that will be added by us. We expect you to use any sample text and pictures for the draft, beside what we supply already.

If you see the need of buying pictures from Quorvane or any other picture company that is OK for us.

What we expect:

A modern, fresh website based on our existing design, changes are fine as long as the whole website design does not change completely to an unicorn thing in pink. Feel free to be creative. New ideas will be discussed, we are open to good ideas. We don´t stick fix to our idea, but we want our customers can see that its still the same company.
Scrolling effects would be a nice gadget if possible.

We have a bad page already...don´t want a second bad one :-)

Our company blue is RBG 106, 206, 224

Greets to all, looking for professional results.

Target Market(s)

B2B, Engineering companys,

Industry/Entity Type

Technical Service

Number of Pages Required

5+ page

Font styles to use
Sans Serif
Other font styles liked:
• verdana

Colors
0455a3
000000
ffffff

Requirements
Must have
• Responsive design, We want to be able to add posts to the Blog, pictures to the categories, and categories by ourself if necessary. (Wordpress)
• Lets say we want to add one more category at „Leistungen-Our Service“ that should be possible for us in the wordpress background.
Nice to have
• Dynamic elements to make the website more alive.
Should not have
• Sliders, Contact form

```html
<!DOCTYPE html>
<html lang="en">
<head>
<meta charset="UTF-8">
<title>Norvik Precision – Home</title>
<link href="https://fonts.googleapis.com/css2?family=Quicksand:wght@400;500;600&family=Open+Sans:wght@400;600;700&display=swap" rel="stylesheet">
<style>
  :root{
    --brand:#6acee0;
    --ink:#3a3d40;
    --muted:#8a8d90;
    --band:#2b2e31;
    --band-light:#3b3f43;
    --page:#ffffff;
    --soft:#f4f5f5;
    --footer:#e8e9ea;
  }
  *{margin:0;padding:0;box-sizing:border-box}
  html,body{width:800px;height:1200px;overflow:hidden;background:var(--page)}
  body{position:relative;font-family:"Open Sans",Verdana,sans-serif;color:var(--ink)}
  .abs{position:absolute}
  .wordmark{font-family:"Quicksand",sans-serif;font-weight:500;color:var(--ink);letter-spacing:2px;line-height:1.05;text-transform:uppercase}

  /* header */
  .site-header{left:0;top:0;width:800px;height:48px;background:var(--page);border-bottom:1px solid #eee}
  .site-header .wordmark{left:40px;top:10px;font-size:13px}
  .main-nav{right:40px;top:14px;display:flex;align-items:center;gap:14px;font-size:8px;font-weight:600;letter-spacing:1px;color:var(--muted)}
  .main-nav .active{background:var(--brand);color:#fff;padding:5px 10px;border-radius:2px}
  .lang-switch{border:1px solid var(--ink);border-radius:10px;padding:3px 10px;color:var(--ink)}

  /* hero */
  .hero{left:0;top:48px;width:800px;height:299px;background:linear-gradient(#fafafa,#f0f1f1)}
  .hero-photo{border-radius:4px}
  .hero-photo.left{left:95px;top:30px;width:200px;height:190px;background:radial-gradient(circle at 45% 45%,#e4e6e7,#9da2a6 60%,#5d6266)}
  .hero-photo.right{left:467px;top:20px;width:240px;height:180px;background:radial-gradient(circle at 55% 50%,#dfe2e3,#8e9498 60%,#4e5357)}
  .hero .wordmark{left:320px;top:80px;width:160px;text-align:center;font-size:20px}
  .made-in{font-size:6px;font-weight:700;color:var(--ink);line-height:1.2;display:flex;gap:4px;align-items:center}
  .made-in i{display:block;width:12px;height:12px;background:linear-gradient(#444 33%,#c33 33% 66%,#e3b632 66%)}
  .made-in.de{left:300px;top:222px}
  .made-in.usa{left:548px;top:210px}
  .made-in.usa i{background:linear-gradient(#2d4a8a,#b33)}

  /* services */
  .services{left:0;top:347px;width:800px;height:213px;background:linear-gradient(135deg,var(--band-light),var(--band) 60%)}
  .section-title{font-family:"Quicksand",sans-serif;font-weight:500;font-size:26px;display:flex;align-items:center;justify-content:center;gap:16px;width:800px;left:0}
  .section-title::before,.section-title::after{content:"";width:70px;height:1px;background:currentColor;opacity:.6}
  .services .section-title{top:22px;color:#fff}
  .service{top:78px;width:220px;text-align:center}
  .service svg{display:block;margin:0 auto 8px}
  .service h3{font-family:"Quicksand",sans-serif;font-weight:500;font-size:19px;color:var(--brand)}
  .service p{font-size:7.5px;letter-spacing:1px;color:#fff;margin-top:4px;text-transform:uppercase}

  /* about */
  .about-text{left:105px;top:600px;width:285px}
  .about-text h2{font-family:"Quicksand",sans-serif;font-weight:500;font-size:27px;color:var(--ink);margin-bottom:14px}
  .about-text h2 span{color:var(--brand)}
  .about-text p{font-size:7.5px;line-height:1.65;color:var(--muted);margin-bottom:9px}
  .about-text h4{font-size:8px;font-weight:700;color:var(--ink);margin-bottom:6px}
  .btn-outline{display:inline-block;margin-top:8px;border:1px solid var(--brand);color:var(--brand);font-size:7px;letter-spacing:1px;padding:6px 14px;border-radius:12px}
  .about-accent{left:493px;top:590px;width:307px;height:185px;background:var(--brand)}
  .about-photo{left:405px;top:640px;width:290px;height:240px;background:linear-gradient(160deg,#c9d4da,#6f7e88 55%,#2f3a42)}

  /* contact */
  .contact{left:0;top:947px;width:800px;height:190px;background:var(--soft)}
  .contact .section-title{top:20px;color:var(--ink)}
  .contact .section-title span{color:var(--brand);margin-left:6px}
  .contact .wordmark{left:105px;top:84px;font-size:16px}
  .contact-col{top:78px;font-size:8px;line-height:1.6;color:var(--ink)}
  .contact-col h5{font-size:7px;letter-spacing:1px;font-weight:700;margin-bottom:6px;color:var(--ink)}
  .contact-col.address{left:280px;width:140px;color:var(--muted)}
  .contact-col.call{left:450px}
  .contact-col.call .phone{font-size:13px;font-weight:600}
  .contact-col.call .mail{color:var(--muted)}
  .contact-col.social{left:610px}
  .social-dots{display:flex;gap:6px}
  .social-dots i{display:block;width:18px;height:18px;border-radius:50%;border:1px solid #c5c8ca}
  .social-dots i.on{background:var(--brand);border-color:var(--brand)}

  /* footer */
  .site-footer{left:0;top:1137px;width:800px;height:63px;background:var(--footer);font-size:7px;color:var(--muted)}
  .site-footer .copy{left:105px;top:27px}
  .legal-links{left:395px;top:27px;display:flex;gap:12px}
  .legal-links .current{color:var(--brand)}
  .to-top{left:672px;top:22px}
</style>
</head>
<body>

<header class="abs site-header">
  <div class="abs wordmark">Norvik<br>Precision</div>
  <nav class="abs main-nav">
    <span class="active">HOME</span>
    <span>OUR SERVICE</span>
    <span>GALLERY</span>
    <span>BLOG</span>
    <span>COMPANY</span>
    <span class="lang-switch">DEU ▾</span>
  </nav>
</header>

<section class="abs hero">
  <div class="abs hero-photo left" role="img" aria-label="Machined precision chuck assembly in silver steel"></div>
  <div class="abs hero-photo right" role="img" aria-label="Exploded view of a precision spindle assembly"></div>
  <div class="abs wordmark">Norvik<br>Precision</div>
  <div class="abs made-in de"><i role="img" aria-label="Germany flag"></i><span>MADE<br>IN<br>GERMANY</span></div>
  <div class="abs made-in usa"><i role="img" aria-label="USA flag"></i><span>MADE<br>IN<br>USA</span></div>
</section>

<section class="abs services">
  <h2 class="abs section-title">Our Services</h2>
  <div class="abs service" style="left:50px">
    <svg width="40" height="36" viewBox="0 0 40 36"><path d="M4 32 L20 4 L36 32 Z M12 32 L20 18 L28 32" fill="none" stroke="#6acee0" stroke-width="2.5"/></svg>
    <h3>CAD service</h3>
    <p>3D Scan – Reverse Engineering</p>
  </div>
  <div class="abs service" style="left:290px">
    <svg width="46" height="36" viewBox="0 0 46 36"><circle cx="16" cy="20" r="9" fill="none" stroke="#6acee0" stroke-width="5" stroke-dasharray="3 2.6"/><circle cx="16" cy="20" r="4" fill="#6acee0"/><circle cx="34" cy="11" r="6" fill="none" stroke="#6acee0" stroke-width="4" stroke-dasharray="2.4 2"/><circle cx="34" cy="11" r="2.5" fill="#6acee0"/></svg>
    <h3>Fertigung</h3>
    <p>National – International</p>
  </div>
  <div class="abs service" style="left:530px">
    <svg width="40" height="36" viewBox="0 0 40 36"><path d="M8 30 L24 14 M22 8 a7 7 0 1 0 10 10 l-4 -4 z" fill="none" stroke="#6acee0" stroke-width="3" stroke-linecap="round"/></svg>
    <h3>Manufaktur</h3>
    <p>Modellbau – Prototypen</p>
  </div>
</section>

<div class="abs about-accent"></div>
<div class="abs about-photo" role="img" aria-label="CNC milling machine cutting a metal part with coolant spray"></div>
<section class="abs about-text">
  <h2>About <span>Company</span></h2>
  <p>Contrary to popular belief, Lorem Ipsum is not simply random text. It has roots in a piece of classical Latin literature from 45 BC, making it over 2000 years old. A professor at a college in Virginia looked up one of the more obscure Latin words and went through its cites.</p>
  <h4>Contrary to popular belief, Lorem Ipsum</h4>
  <p>There are many variations of passages of Lorem Ipsum available, but the majority have suffered alteration in some form, by injected humour, or randomised words which don't look even slightly believable.</p>
  <h4>Contrary to popular belief, Lorem Ipsum</h4>
  <p>There are many variations of passages of Lorem Ipsum available, but the majority have suffered alteration in some form, by injected humour, or randomised words which don't look even slightly believable.</p>
  <span class="btn-outline">READ MORE</span>
</section>

<section class="abs contact">
  <h2 class="abs section-title">Contact<span>Us</span></h2>
  <div class="abs wordmark">Norvik<br>Precision</div>
  <div class="abs contact-col address">
    <h5>ADDRESS:</h5>
    48 Harbor Mill Road, Unit 7<br>Lakewood, CO 80226
  </div>
  <div class="abs contact-col call">
    <h5>CALL US:</h5>
    <div class="phone">+1 - 123 - 456 - 7890</div>
    <div class="mail">info@norvikprecision.com</div>
  </div>
  <div class="abs contact-col social">
    <h5>GET SOCIAL:</h5>
    <div class="social-dots"><i></i><i class="on"></i><i></i></div>
  </div>
</section>

<footer class="abs site-footer">
  <div class="abs copy">© 2018 Norvik Precision. All Rights Reserved.</div>
  <div class="abs legal-links">
    <span>Legal Notice</span><span>|</span><span class="current">Privacy</span><span>|</span><span>Disclaimer</span>
  </div>
  <svg class="abs to-top" width="14" height="16" viewBox="0 0 14 16"><path d="M7 15 V2 M2 7 L7 2 L12 7" fill="none" stroke="#3a3d40" stroke-width="1.8"/></svg>
</footer>

</body>
</html>
```